MCP phase 1 web design

Meridale Capital Partners Ltd (MCP) is a challenger business to the traditional leasing market. We look for solutions to complex problems involving the funding of capital equipment within an office environment and then build documentation around the solution. We recently created a brief for a logo and successfully completed that assignment. We now need to create our first web site which is simply intended to be informative. To help interested designers we have attached a detailed brief that is broken into three sections. The first explains how we see the site developing over time from something quite straightforward initially to a full transaction capability. Whoever wins this competition will be expected to work with us into the future to help develop the site. Section 2 gives you a view about our likes and dislikes by reviewing some existing sites. Section 3 gives you the structure and content of the site based upon our likes and dislikes. We are by no means committed to the structure and if you believe it can be presented in a better way then please use your design. The text is fixed as content. The images to appear can be anything from photographs to line drawings again entirely at the designers whim. Currently we have a home page plus 5 subsidiary pages. A few things to help you:
1. The logo is fixed and should be amongst the downloads.
2. The colours we have are corporate and should be used.
3. The typeface we use within the business is "Verdana"
Good luck.

```html
<!DOCTYPE html>
<html lang="en">
<head>
<meta charset="utf-8">
<title>Meridale Capital Partners Ltd</title>
<link href="https://fonts.googleapis.com/css2?family=Lato:ital,wght@0,400;0,700;1,400&display=swap" rel="stylesheet">
<style>
:root{
  --blue:#1f75c0;
  --blue-dark:#1a5fa0;
  --ink:#2a2a2a;
  --text:#555;
  --dark:#3d3c42;
  --grey-panel:#e9e9e9;
  --line:#ddd;
  --white:#fff;
}
*{margin:0;padding:0;box-sizing:border-box}
html,body{width:1200px;height:1163px;overflow:hidden}
body{position:relative;font-family:"Lato",Verdana,sans-serif;background:var(--white);color:var(--ink)}
.abs{position:absolute}

/* header */
.site-header{position:absolute;left:0;top:0;width:1200px;height:98px;background:linear-gradient(#fff,#ebebeb);box-shadow:0 2px 4px rgba(0,0,0,.35);z-index:3}
.brand{position:absolute;left:145px;top:30px;display:flex;align-items:center;gap:10px}
.brand-mark{width:30px;height:30px;border-radius:50%;background:var(--blue)}
.brand-name{font-size:22px;font-weight:400;color:var(--blue);letter-spacing:.5px;line-height:1.1}
.main-nav{position:absolute;top:38px;left:599px;display:flex;align-items:center;font-size:15px;color:#333}
.main-nav a{text-decoration:none;color:#333;padding:0 20px;border-left:1px solid #d6d6d6;line-height:18px}
.main-nav a:first-child{border:0}
.main-nav a.active{background:var(--blue);color:#fff;border-radius:3px;padding:4px 10px;line-height:18px;margin-right:10px}

/* hero */
.hero-band{position:absolute;left:0;top:98px;width:1200px;height:492px;background:var(--dark)}
.hero{position:absolute;left:141px;top:123px;width:918px;height:477px;border-radius:6px 6px 0 0;overflow:hidden}
.hero-photo{position:absolute;inset:0;background:radial-gradient(ellipse at 38% 45%,#dfe9f3 0%,#98b3cf 45%,#5e7fa6 100%)}
.hero-photo::before{content:"";position:absolute;left:0;top:0;width:300px;height:100%;background:linear-gradient(90deg,#8f4a3c,rgba(180,110,90,0));opacity:.55}
.hero-copy{position:absolute;left:541px;top:76px;width:351px;height:261px;background:rgba(255,255,255,.88);border-radius:3px;padding:22px 16px;font-size:14px;font-weight:700;line-height:21px;color:#111}
.hero-copy .hl{color:var(--blue)}
.hero-copy .tracked{letter-spacing:1.3px}
.hero-copy p+p{margin-top:21px}
.slider-dots{position:absolute;left:427px;top:401px;display:flex;gap:7px}
.slider-dots span{width:12px;height:12px;border-radius:50%;background:#d8d8d8}
.slider-dots span.on{background:var(--blue)}
.hero-curve{position:absolute;left:0;bottom:0}

/* services */
.services{position:absolute;left:141px;top:590px;width:918px;height:169px;background:#fff;box-shadow:0 3px 6px rgba(0,0,0,.12);border-radius:0 0 3px 3px}
.service{position:absolute;top:20px}
.service h2{font-size:19px;font-weight:700;color:#333;white-space:nowrap}
.service .icon{position:absolute;top:36px;width:75px;height:75px;border-radius:50%;background:var(--blue)}
.service p{position:absolute;top:38px;width:185px;font-size:13.5px;line-height:18.5px;color:#666}
.service .more{position:absolute;top:128px;font-size:13px;font-weight:700;color:#1b2a3a;white-space:nowrap}
.divider{position:absolute;top:24px;width:1px;height:110px;background:var(--line)}

/* welcome */
.welcome{position:absolute;left:141px;top:800px;width:586px}
.welcome-title{display:flex;align-items:center;height:38px}
.welcome-title .tag{font-size:18px;font-weight:700;color:var(--blue);padding-right:10px;border-right:1px solid #ccc;margin-right:10px;margin-left:2px}
.welcome-title h1{font-size:24px;font-weight:400;color:#444}
.welcome-title h1 span{color:var(--blue)}
.dash{position:absolute;top:48px;left:0;width:586px;border-top:1px dashed #aaa}
.lead{position:absolute;top:64px;left:2px;font-size:13px;font-weight:700;color:#222}
.body-copy{position:absolute;top:92px;left:2px;width:584px;font-size:13.2px;line-height:21px;color:#444}
.welcome .more{position:absolute;top:205px;right:10px;font-size:13px;font-weight:700;color:#1b2a3a}
.col-rule{position:absolute;left:753px;top:815px;width:1px;height:185px;background:linear-gradient(transparent,#ccc 20%,#ccc 80%,transparent)}

/* stories */
.stories{position:absolute;left:778px;top:807px;width:281px}
.stories-head{height:40px;background:var(--grey-panel);font-size:21px;padding:6px 11px;color:#222;position:relative}
.stories-head::after{content:"";position:absolute;left:26px;bottom:-8px;border:8px solid transparent;border-bottom:0;border-top-color:var(--grey-panel)}
.quote{position:absolute;top:60px;left:3px;width:280px;font-size:13px;font-style:italic;line-height:21px;color:#444;text-indent:21px}
.quote-mark{position:absolute;top:60px;left:3px;font-size:34px;line-height:30px;color:#c8c8c8;font-style:normal}
.author{position:absolute;top:150px;left:3px;font-size:13px;font-weight:700;color:#222}
.role{position:absolute;top:173px;left:3px;font-size:13px;font-style:italic;color:#777}
.role a{color:var(--blue);text-decoration:none}
.stories .more{position:absolute;top:206px;right:0;font-size:13px;font-weight:700;color:#1b2a3a}

/* footer */
.site-footer{position:absolute;left:0;top:1059px;width:1200px;height:104px;background:var(--dark);border-top:5px solid var(--blue)}
.footer-welcome{position:absolute;left:143px;top:48px;font-size:17px;color:#fff}
.footer-brand{position:absolute;right:141px;top:32px;font-size:19px;color:#fff;white-space:nowrap}
.copyright{position:absolute;right:138px;top:77px;font-size:9px;color:#ccc}
</style>
</head>
<body>

<header class="site-header">
  <div class="brand"><span class="brand-mark"></span><span class="brand-name">Meridale Capital Partners</span></div>
  <nav class="main-nav">
    <a class="active" href="#">HOME</a>
    <a href="#">WHY MERIDALE</a>
    <a href="#">SOLUTIONS</a>
    <a href="#">CONTACT</a>
  </nav>
</header>

<div class="hero-band"></div>
<section class="hero">
  <div class="hero-photo" role="img" aria-label="Close-up photo of fingers placing a blue jigsaw puzzle piece into a puzzle"></div>
  <div class="hero-copy">
    <p><span class="tracked">We provide <span class="hl">"Sales Aid Finance"</span> through</span> <span class="hl">MERIDALE</span> financial and contract solutions. Specialising in the Print and Technology markets, we offer <span class="hl">Value Added Resellers (VARs)</span> a range of innovative, cost effective, value added contract and finance options to enhance their sales.</p>
    <p>Our solutions are fully financed and we are totally independent from any VAR, technology provider or traditional finance house.</p>
  </div>
  <div class="slider-dots"><span class="on"></span><span></span><span></span><span></span></div>
  <svg class="hero-curve" width="918" height="60" viewBox="0 0 918 60">
    <path d="M0 50 Q459 -20 918 50 L918 60 L0 60 Z" fill="#fff"/>
    <path d="M0 46 Q459 -26 918 46 L918 60 Q459 -8 0 60 Z" fill="#1f75c0"/>
  </svg>
</section>

<section class="services">
  <div class="service" style="left:15px">
    <h2>Managed Services Solutions</h2>
    <svg class="icon" style="left:-4px" viewBox="0 0 75 75">
      <circle cx="37.5" cy="37.5" r="37.5" fill="#1f75c0"/>
      <g fill="#fff">
        <circle cx="30" cy="44" r="11"/><circle cx="48" cy="27" r="7.5"/>
        <g stroke="#fff" stroke-width="5"><path d="M30 28v32M14 44h32M19 33l22 22M41 33l-22 22"/><path d="M48 16v22M37 27h22M40 19l16 16M56 19l-16 16" stroke-width="3.5"/></g>
      </g>
      <circle cx="30" cy="44" r="4.5" fill="#1f75c0"/><circle cx="48" cy="27" r="3" fill="#1f75c0"/>
    </svg>
    <p style="left:83px">Large enterprises, as well as SMEs, non-for profit and most Public Sector organisations, ask for flexibility ...</p>
    <span class="more" style="left:196px">Read more »</span>
  </div>
  <div class="divider" style="left:298px"></div>
  <div class="service" style="left:330px">
    <h2>Public Sector Solutions</h2>
    <svg class="icon" style="left:1px" viewBox="0 0 75 75">
      <circle cx="37.5" cy="37.5" r="37.5" fill="#1f75c0"/>
      <g fill="#fff">
        <circle cx="37.5" cy="27" r="7"/><path d="M24 52c0-11 6-16 13.5-16S51 41 51 52z"/>
        <circle cx="22" cy="31" r="5.5"/><path d="M11 50c0-8 4-12 11-12 3 0 4 1 5 1-3 3-4 7-4 11z"/>
        <circle cx="53" cy="31" r="5.5"/><path d="M64 50c0-8-4-12-11-12-3 0-4 1-5 1 3 3 4 7 4 11z"/>
      </g>
    </svg>
    <p style="left:95px">Most public sector bodies increasingly require contract flexibility. In particular, some large tender frameworks ...</p>
    <span class="more" style="left:202px">Read more »</span>
  </div>
  <div class="divider" style="left:618px"></div>
  <div class="service" style="left:650px">
    <h2>Education Solutions</h2>
    <svg class="icon" style="left:2px" viewBox="0 0 75 75">
      <circle cx="37.5" cy="37.5" r="37.5" fill="#1f75c0"/>
      <g fill="#fff">
        <path d="M37.5 16 62 27 37.5 38 13 27z"/><path d="M24 33v10c4 4 22 4 27 0V33l-13.5 6z"/>
        <path d="M15 48c8-3 16-2 22.5 3 6.5-5 14.5-6 22.5-3v10c-8-3-16-2-22.5 3-6.5-5-14.5-6-22.5-3z"/>
        <rect x="58" y="27" width="2" height="14"/>
      </g>
    </svg>
    <p style="left:97px">Using the right type of financial product is essential for technology projects in the Education sector.</p>
    <span class="more" style="left:194px">Read more »</span>
  </div>
</section>

<section class="welcome">
  <div class="welcome-title"><span class="tag">MCP</span><h1>Welcome to <span>Meridale Capital Partners Ltd</span></h1></div>
  <div class="dash"></div>
  <p class="lead">Lorem ipsum dolor sit amet, consectetuer adipiscing elit, sed diam nonummy nibh euismod.</p>
  <p class="body-copy">Consectetuer adipiscing elit, sed diam nonummy nibh euismod tincidunt ut laoreet dolore ma aliqua erat volutpat. Ut wisi enim ad minim veniam, quis nostrud exerci tation ullamcorper suscipit lob nisl ut aliquip ex ea commodo consequat. Duis autem vel eum iriure dolor in hendrerit in vulputate esse molestie consequat, vel illum dolore eu feugiat nulla facilisis at vero eros et accumsan et iu dignissim qui blandit praesent luptatum zzril delenit augue duis dolore te feugait nulla facilisi.</p>
  <span class="more">Read more »</span>
</section>

<div class="col-rule"></div>

<aside class="stories">
  <div class="stories-head">Customer Stories</div>
  <span class="quote-mark">“</span>
  <p class="quote">Consectetuer adipiscing elit, sed diam nonum nibh euismod tincidunt ut laoreet dolore aliqua er volutpat. Ut wisi enim ad minim veniam, nostrud exerci tation ullamcorper suscipit lob.</p>
  <p class="author">Tom Harwell</p>
  <p class="role">Marketing Manager - <a href="#">Company name</a></p>
  <span class="more">Read more »</span>
</aside>

<footer class="site-footer">
  <p class="footer-welcome">Welcome to Meridale Capital Partners</p>
  <p class="footer-brand">Meridale Capital Partners</p>
  <p class="copyright">© 2014 Meridale CP ltd. All Rights Reserved.</p>
</footer>

</body>
</html>
```